I need a book cover for a non-fiction book, entitled "Walk The Meadow Path and GLOW" (the "GLOW" is an acronym for "Gather Old Lantern Works" [but needn't {and probably shouldn't} be on the cover]).
The book will be 7" W X 10" H, in hardcover, and the spine will be 1.3" thick [just under "1-5/16"]).
When completed, I'll eventually need artwork for a full spread--of 16.874" W X 11.417" H--for back, spine and front artwork (see the two files attached, for specifics on final layout [feel free to concentrate only on the front cover, for the run-off selection process]).
The front cover by itself will measure 7.197" X 10.236" with bleed, trimmed to 7" X 10" for final size.
On the spine, the book title and author's last name (Pruitt) will be sufficient.
Author's name (Dale Pruitt) on the front cover, near the bottom/ bottom right, without great emphasis, generally preferred.
Don't need to worry about the back cover until finalists picked. I'll want a heading up top being probably a smaller version of the title.
In the body of the back page, I'll be putting in a text block (if necessary, to see the text), unless the background color is very light. Don't worry about having any graphics to speak of on the back, other than general light color, or screened image.
There will be a UPC bar code on the lower right of the back cover, also.

The book itself teaches the U.S. Constitution, to readers, covering the originally-ratified document (but not covering the amendments, which will be a separate volume, later), the founding principles of our American Republic (which doesn't rely upon voting or elections--Democracy--to uphold [so please don't emphasize the voting process in the artwork]).
A sincere patriotic theme (and colors, likely) would be preferred, along strict-construction themes (limited government of delegated powers, implemented using only necessary and proper means, to promote individual liberty and secured unalienable rights).
Christian perspective.
The Constitution, Bill of Rights, and Declaration of Independence are of course good graphics to include (but not any contemporary redesign of them).
American flags, eagles, gold and silver coin (but must be American-struck gold or silver coin design, from BEFORE 1933 [NOT the recent Harbor Finch bullion gold coins, or bullion silver eagles [which are coins, in 1 oz. weight, and its increments]) and historical-themed images of the Revolutionary era are fine, historical buildings okay, Liberty Bell okay. Statue of Liberty probably less desirable (since it doesn't directly relate to the Founders of the country, or the Framers of the Constitution, Bill of Rights, Declaration of Independence directly [even as it was meant to symbolize and honor them]).

The book is a compilation of my WalkTheMeadowPathEachSeason Program Course, an online video/audio/pdf Lesson that teaches the Constitution in one year (www.WalkTheMeadowPathEachSeason.com)

Patriotic conservative Christian men and women, typically older (but even older teens and young adults and serious college students

• Conservative patriot theme

```html
<!DOCTYPE html>
<html lang="en">
<head>
<meta charset="utf-8">
<title>Walk The Meadow Path and GLOW — Front Cover</title>
<link href="https://fonts.googleapis.com/css2?family=Oranienbaum&family=Oswald:wght@500&display=swap" rel="stylesheet">
<style>
  :root {
    --stage: #0c2960;
    --cover-deep: #0a1f56;
    --cover-mid: #173279;
    --gold: #e8b65e;
    --coin-gold: #c9973a;
    --coin-light: #e6bd62;
    --coin-shadow: #081a4a;
    --author: #ffffff;
  }
  html, body {
    margin: 0;
    padding: 0;
    width: 1200px;
    height: 721px;
    overflow: hidden;
    background: var(--stage);
  }
  .stage {
    width: 1200px;
    height: 721px;
    display: flex;
    align-items: center;
    justify-content: center;
  }
  .front-cover {
    width: 462px;
    height: 660px;
    display: block;
    box-shadow: 0 18px 40px rgba(0, 0, 0, 0.35);
  }
  .title-line {
    font-family: "Oranienbaum", "Times New Roman", serif;
    fill: var(--gold);
  }
  .author-name {
    font-family: "Oswald", "Arial Narrow", sans-serif;
    font-weight: 500;
    fill: var(--author);
    letter-spacing: 7px;
  }
</style>
</head>
<body>
<main class="stage">
  <svg class="front-cover" viewBox="0 0 462 660" xmlns="http://www.w3.org/2000/svg" aria-labelledby="cover-title">
    <title id="cover-title">Walk the Meadow Path &amp; Glow by Dale Pruitt</title>
    <defs>
      <radialGradient id="cover-surface" cx="0.4" cy="0.35" r="0.85">
        <stop offset="0" stop-color="var(--cover-mid)"/>
        <stop offset="1" stop-color="var(--cover-deep)"/>
      </radialGradient>
      <radialGradient id="coin-tone" cx="0.4" cy="0.35" r="0.7">
        <stop offset="0" stop-color="var(--coin-light)"/>
        <stop offset="1" stop-color="var(--coin-gold)"/>
      </radialGradient>
    </defs>

    <rect class="cover-ground" width="462" height="660" fill="url(#cover-surface)"/>

    <g class="cover-title">
      <text class="title-line" x="118" y="150" font-size="98" textLength="160" lengthAdjust="spacingAndGlyphs">WALK</text>
      <text class="title-line" x="290" y="150" font-size="50" textLength="52" lengthAdjust="spacingAndGlyphs">the</text>
      <text class="title-line" x="18" y="268" font-size="104" textLength="426" lengthAdjust="spacingAndGlyphs">MEADOW PATH</text>
      <text class="title-line" x="128" y="378" font-size="52">&amp;</text>
      <text class="title-line" x="168" y="378" font-size="100" textLength="156" lengthAdjust="spacingAndGlyphs">GLOW</text>
    </g>

    <g class="cover-coin" role="img" aria-label="Antique American gold coin, profile side, dated before 1933">
      <circle cx="243" cy="472" r="80" fill="var(--coin-shadow)"/>
      <circle cx="230" cy="468" r="80" fill="url(#coin-tone)"/>
    </g>

    <text class="author-name" x="231" y="610" font-size="30" text-anchor="middle">DALE PRUITT</text>
  </svg>
</main>
</body>
</html>
```